Tarvimoor business cards

Need fresh design for our business cards. Logo must be specific, we are open for everything else.

Contact Information for Business Card

phrase "GMP & JANITORIAL SERVICES" should be used as main point of card

Colors
3176b5
3276b5
85acd3
cedeed
ffffff
0292cd
33a6d7
85cae6
cee9f5

Requirements
Must have
• The logo
Should not have
• crowded designs

```html
<!DOCTYPE html>
<html lang="en">
<head>
<meta charset="utf-8">
<title>Tarvimoor business cards</title>
<link href="https://fonts.googleapis.com/css2?family=Lato:wght@400;700&display=swap" rel="stylesheet">
<style>
  :root {
    --brand-blue: #0880c2;
    --paper: #ffffff;
    --ink: #1e1e1e;
    --backdrop: #bdbdbd;
    --card-shadow: rgba(0, 0, 0, 0.35);
  }
  * { margin: 0; padding: 0; box-sizing: border-box; }
  html, body {
    width: 1200px; height: 802px; overflow: hidden;
    background: var(--backdrop);
    font-family: "Lato", Arial, sans-serif;
  }
  .canvas { position: relative; width: 1200px; height: 802px; }
  .card {
    position: absolute; top: 274px;
    width: 443px; height: 265px;
    box-shadow: 2px 3px 6px var(--card-shadow);
    overflow: hidden;
  }
  .card--front { left: 136px; background: var(--paper); }
  .card--back { left: 624px; background: var(--brand-blue); }

  .front-band {
    position: absolute; left: 0; top: 0; width: 100%; height: 77px;
    background: var(--brand-blue);
  }
  .lockup {
    position: absolute; display: flex; flex-direction: column; align-items: flex-end;
    color: var(--paper); white-space: nowrap;
  }
  .wordmark { font-weight: 400; letter-spacing: 0.12em; line-height: 1; }
  .tagline { font-weight: 700; letter-spacing: 0.2em; line-height: 1; }

  .front-band .lockup { left: 27px; top: 21px; }
  .front-band .wordmark { font-size: 28px; }
  .front-band .tagline { font-size: 7px; margin-top: 3px; margin-right: 3px; }

  .card--back .lockup { left: 50%; top: 116px; transform: translateX(-50%); }
  .card--back .wordmark { font-size: 39px; }
  .card--back .tagline { font-size: 9px; margin-top: 4px; margin-right: 4px; }

  .person { position: absolute; left: 24px; top: 139px; }
  .person-name {
    color: var(--brand-blue); font-weight: 700; font-size: 18px; line-height: 20px;
  }
  .person-role { color: var(--ink); font-size: 12.5px; line-height: 14px; }

  .contact-list {
    position: absolute; left: 24px; top: 181px; list-style: none;
    color: var(--ink); font-size: 13px; line-height: 16px;
  }
  .contact-list li { display: flex; align-items: center; gap: 4px; }
  .contact-list svg { width: 10px; height: 10px; fill: var(--brand-blue); flex: none; }

  .address {
    position: absolute; right: 28px; top: 213px; text-align: right;
    color: var(--ink); font-size: 13px; line-height: 16px; font-style: normal;
  }
</style>
</head>
<body>
<main class="canvas">
  <section class="card card--front" aria-label="Card front">
    <div class="front-band">
      <div class="lockup">
        <span class="wordmark">TARVIMOOR</span>
        <span class="tagline">GMP &amp; JANITORIAL SERVICES</span>
      </div>
    </div>
    <div class="person">
      <p class="person-name">DANIEL HARTLEY</p>
      <p class="person-role">Managing Director</p>
    </div>
    <ul class="contact-list">
      <li>
        <svg viewBox="0 0 10 10" aria-hidden="true"><path d="M1 3.2C1 2 2.5 1.3 5 1.3S9 2 9 3.2v.8H7V3.2H3V4H1z M2.5 4.5h5L9 8.7H1z"/></svg>
        044-555 210 486
      </li>
      <li>
        <svg viewBox="0 0 10 10" aria-hidden="true"><path d="M3 0.5h4a.8.8 0 0 1 .8.8v7.4a.8.8 0 0 1-.8.8H3a.8.8 0 0 1-.8-.8V1.3A.8.8 0 0 1 3 .5zm.3 1.2v5.8h3.4V1.7z"/></svg>
        044-555 210 487
      </li>
      <li>
        <svg viewBox="0 0 10 10" aria-hidden="true"><path d="M0.5 2h9v6h-9z M1.2 2.6 5 5.6l3.8-3" stroke="#fff" stroke-width=".8"/></svg>
        info@tarvimoor.com
      </li>
      <li>
        <svg viewBox="0 0 10 10" aria-hidden="true"><circle cx="5" cy="5" r="4.5"/><path d="M2.5 3.5 4 3l1 1.5-1 1.5L5 8 3.3 6.5z M6 2l1.8 1.2-.5 1.5L6 4z" fill="#fff"/></svg>
        www.tarvimoor.com
      </li>
    </ul>
    <address class="address">
      48 Harbour Lane<br>
      Northfield, 204816
    </address>
  </section>

  <section class="card card--back" aria-label="Card back">
    <div class="lockup">
      <span class="wordmark">TARVIMOOR</span>
      <span class="tagline">GMP &amp; JANITORIAL SERVICES</span>
    </div>
  </section>
</main>
</body>
</html>
```